Social Health & Parkinson's

I need a 1-pg horizontal infographic that can be handed out to patients and providers. It needs to be scientifically sound (data provided), easy to understand, and visually pleasing. Target audience; patiens (mostly 40-90 years old) and providers (neurologists, nurses, physical therapists, naturopathic physicians, support group leaders, etc.) We need 6 of these, one for each topic listed on the website. Ideally, we'll hire the winner for 5 more similar projects and keep a theme.

Target Market(s)

Patients with Parkinson's disease, their families, care providers. To be handed out by physicians, support group leaders, etc.

Colors

Designer to choose colors to be used in the design.

Requirements
Must have
• Visually stunning. Data integrity-- keep the numbers and the figures we provide. Reference to where the data is coming from. Be thoughtful of elderly, vision issues. Teach everyone something.

```html
<!DOCTYPE html>
<html lang="en">
<head>
<meta charset="utf-8">
<title>Social Health &amp; Patient Reported Outcomes in Parkinson's Disease</title>
<link href="https://fonts.googleapis.com/css2?family=Merriweather:wght@400;700;900&family=Source+Sans+3:ital,wght@0,400;0,600;0,700;1,400;1,600;1,700&display=swap" rel="stylesheet">
<style>
  :root{
    --stage:#ebe6f0;
    --card:#f3f3f3;
    --purple:#5f2b8c;
    --purple-deep:#4a1f73;
    --pink:#f2c4d5;
    --blue-panel:#cadded;
    --ink:#1f1f1f;
    --muted:#3a3a3a;
    --teal:#a9dbd0;
    --red:#c3192d;
    --red-deep:#b0111c;
    --red-soft:#d8394c;
    --navy:#2c2a8c;
    --green:#78b833;
    --green-mid:#8cc63f;
    --green-soft:#a9d07c;
    --orange:#f0931e;
    --fair-blue:#2a78c2;
    --lime:#c6d63a;
    --axis-grey:#c9c9c9;
    --serif:'Merriweather', Georgia, serif;
    --sans:'Source Sans 3', Arial, sans-serif;
  }
  html,body{margin:0;padding:0;}
  body{width:1200px;height:1026px;overflow:hidden;background:var(--stage);position:relative;}
  .infographic{position:absolute;left:10px;top:59px;width:1180px;height:907px;display:block;}
  .panel-heading{font-family:var(--serif);font-weight:700;font-size:13.5px;fill:var(--ink);text-anchor:middle;}
  .hero-title{font-family:var(--serif);font-weight:700;font-size:24.5px;fill:#fff;}
  .hero-year{font-family:var(--serif);font-weight:700;font-size:21px;fill:var(--purple);}
  .hero-note{font-family:var(--sans);font-style:italic;font-size:14.5px;fill:#fff;}
  .hero-url{font-family:var(--serif);font-size:14px;fill:#fff;}
  .tick{font-family:var(--sans);font-style:italic;font-weight:600;font-size:10.5px;fill:var(--ink);}
  .tick-end{text-anchor:end;}
  .tick-mid{text-anchor:middle;}
  .axis-title{font-family:var(--sans);font-style:italic;font-weight:600;font-size:11.5px;fill:var(--ink);text-anchor:middle;}
  .bubble-label{font-family:var(--sans);font-weight:700;font-size:10px;fill:var(--ink);}
  .pill-text{font-family:var(--sans);font-style:italic;font-weight:600;font-size:12px;fill:#fff;text-anchor:middle;}
  .pill-text-sm{font-size:9.5px;}
  .point-label{font-family:var(--sans);font-style:italic;font-weight:600;font-size:10px;text-anchor:middle;}
  .caption{font-family:var(--sans);font-style:italic;font-size:10.5px;fill:var(--ink);text-anchor:middle;}
  .section-label{font-family:var(--sans);font-style:italic;font-weight:600;font-size:12.5px;}
  .question{font-family:var(--sans);font-style:italic;font-size:10px;fill:var(--ink);}
  .bar-value{font-family:var(--serif);font-weight:700;font-size:12px;fill:var(--ink);text-anchor:middle;}
  .bar-name{font-family:var(--sans);font-size:9.5px;fill:var(--ink);text-anchor:middle;}
  .grid-tick{font-family:var(--sans);font-size:9.5px;fill:var(--ink);text-anchor:end;}
  .variable-name{font-family:var(--sans);font-style:italic;font-size:10px;fill:var(--ink);}
  .impact-neg{font-family:var(--serif);font-weight:700;font-size:12px;fill:var(--green);}
  .impact-pos{font-family:var(--serif);font-weight:700;font-size:12px;fill:var(--red-deep);}
  .findings{font-family:var(--sans);font-style:italic;font-size:10px;fill:var(--ink);text-anchor:end;}
  .scale-tick{font-family:var(--sans);font-weight:600;font-size:10px;fill:var(--ink);text-anchor:middle;}
  .scale-end{font-family:var(--sans);font-size:9.5px;fill:var(--ink);text-anchor:middle;}
</style>
</head>
<body>
<svg class="infographic" viewBox="212 228 1078 829" xmlns="http://www.w3.org/2000/svg" role="img" aria-label="Infographic: Social Health and Patient Reported Outcomes in Parkinson's Disease">
  <defs>
    <linearGradient id="green-bar" x1="0" x2="1" y1="0" y2="0">
      <stop offset="0" stop-color="#8cc63f" stop-opacity="0.15"/>
      <stop offset="0.5" stop-color="#8cc63f"/>
      <stop offset="1" stop-color="#6fae2d"/>
    </linearGradient>
    <linearGradient id="red-bar" x1="0" x2="1" y1="0" y2="0">
      <stop offset="0" stop-color="#b0111c"/>
      <stop offset="0.55" stop-color="#c8283a"/>
      <stop offset="1" stop-color="#f2c4d5"/>
    </linearGradient>
    <linearGradient id="chart-bg" x1="0" x2="0" y1="0" y2="1">
      <stop offset="0" stop-color="#ececec"/>
      <stop offset="1" stop-color="#d9d9d9"/>
    </linearGradient>
  </defs>

  <!-- card -->
  <rect class="card" x="212" y="228" width="1078" height="829" fill="var(--card)"/>

  <!-- hero panel -->
  <g class="panel panel-hero">
    <rect x="234" y="248" width="345" height="348" fill="var(--pink)"/>
    <path d="M234 256 H498 Q506 256 510 263 L518 279 H579 V596 H234 Z" fill="var(--purple)"/>
    <text class="hero-year" x="544" y="272" text-anchor="middle">2020</text>
    <text class="hero-title" x="250" y="333">Social Health &amp; Patient</text>
    <text class="hero-title" x="250" y="362">Reported Outcomes in</text>
    <text class="hero-title" x="250" y="391">Parkinson's Disease</text>
    <text class="hero-note" x="250" y="417">RM Calder et al.</text>
    <g fill="#fff"><circle cx="252" cy="452" r="2"/><circle cx="259" cy="452" r="2"/><circle cx="266" cy="452" r="2"/></g>
    <text class="hero-note" x="250" y="496">For study details:</text>
    <text class="hero-url" x="250" y="516">www.ThrivingWithPDInfo.org</text>
    <text class="hero-note" x="250" y="545">To participate in this study:</text>
    <text class="hero-url" x="250" y="565">www.PDCareStudy.Northlake.edu</text>
  </g>

  <!-- correlation panel -->
  <g class="panel panel-correlation">
    <text class="panel-heading" x="749" y="277">Correlation Between</text>
    <text class="panel-heading" x="749" y="295">Quality of Life and PRO-PD Score</text>
    <path d="M659 333 V537 H890" fill="none" stroke="var(--teal)" stroke-width="12" stroke-linecap="round" stroke-linejoin="round"/>
    <g class="tick tick-end">
      <text x="648" y="341">2500</text><text x="648" y="384">2000</text><text x="648" y="427">1500</text>
      <text x="648" y="470">1000</text><text x="648" y="513">500</text>
    </g>
    <g class="tick tick-mid">
      <text x="645" y="557">0</text><text x="674" y="557">5</text><text x="706" y="557">10</text><text x="741" y="557">15</text>
      <text x="776" y="557">20</text><text x="811" y="557">25</text><text x="846" y="557">30</text><text x="881" y="557">35</text>
    </g>
    <text class="axis-title" x="747" y="579">Year Since Diagnosis</text>
    <text class="axis-title" transform="translate(599 443) rotate(-90)">Patient-Reported Outcomes in PD</text>
    <text class="axis-title" transform="translate(612 443) rotate(-90)">(PRO-PD)</text>

    <g class="bubble bubble-poor">
      <circle cx="853" cy="377" r="22" fill="#fff"/>
      <path d="M833 385 H873 A22 22 0 0 1 833 385 Z" fill="#f2c4d5"/>
      <circle cx="853" cy="377" r="22" fill="none" stroke="var(--red)" stroke-width="5"/>
      <text class="bubble-label" x="826" y="380" text-anchor="end">POOR</text>
    </g>
    <g class="bubble bubble-fair">
      <circle cx="804" cy="430" r="16" fill="#fff"/>
      <path d="M789 434 H819 A16 16 0 0 1 789 434 Z" fill="#c8ced6"/>
      <circle cx="804" cy="430" r="16" fill="none" stroke="var(--fair-blue)" stroke-width="5"/>
      <text class="bubble-label" x="832" y="434">FAIR</text>
    </g>
    <g class="bubble bubble-good">
      <circle cx="747" cy="472" r="14" fill="#fff"/>
      <path d="M733 475 H761 A14 14 0 0 1 733 475 Z" fill="#d3c4e0"/>
      <circle cx="747" cy="472" r="14" fill="none" stroke="#6a3a94" stroke-width="5"/>
      <text class="bubble-label" x="770" y="477">GOOD</text>
    </g>
    <g class="bubble bubble-excellent">
      <circle cx="687" cy="509" r="8" fill="#eef3c6" stroke="var(--lime)" stroke-width="4"/>
      <text class="bubble-label" x="705" y="513">EXCELLENT</text>
    </g>
  </g>

  <!-- loneliness panel -->
  <g class="panel panel-loneliness">
    <rect x="923" y="248" width="346" height="348" fill="var(--pink)"/>
    <text class="panel-heading" x="1108" y="277">Loneliness is Associated with</text>
    <text class="panel-heading" x="1108" y="295">More Severe PD Symptoms</text>
    <path d="M990 330 V540 H1242" fill="none" stroke="var(--ink)" stroke-width="1.5"/>
    <g class="tick tick-end">
      <text x="984" y="335">1400</text><text x="984" y="366">1200</text><text x="984" y="398">1000</text><text x="984" y="429">800</text>
      <text x="984" y="461">600</text><text x="984" y="492">400</text><text x="984" y="524">200</text>
    </g>
    <g class="tick tick-mid">
      <text x="981" y="556">0</text><text x="1004" y="556">1</text><text x="1030" y="556">2</text><text x="1055" y="556">3</text>
      <text x="1080" y="556">4</text><text x="1105" y="556">5</text><text x="1131" y="556">6</text><text x="1157" y="556">7</text>
      <text x="1182" y="556">8</text><text x="1210" y="556">9</text><text x="1236" y="556">10</text>
    </g>
    <text class="axis-title" x="1097" y="579">Year Since Diagnosis</text>
    <text class="axis-title" transform="translate(949 442) rotate(-90)">PD Symptom Severity</text>
    <polyline points="990,394 1017,409 1033,397 1050,406 1118,366 1182,391 1212,358 1242,359" fill="none" stroke="var(--red)" stroke-width="2"/>
    <polyline points="990,485 1024,469 1040,471 1070,465 1083,469 1100,469 1118,471 1142,461 1170,456 1190,452 1210,452 1242,447" fill="none" stroke="var(--navy)" stroke-width="2"/>
    <rect x="1009" y="372" width="64" height="16" rx="8" fill="var(--red)"/>
    <text class="pill-text" x="1041" y="384">Lonely</text>
    <rect x="1151" y="469" width="78" height="16" rx="8" fill="var(--navy)"/>
    <text class="pill-text" x="1190" y="481">Not Lonely</text>
  </g>

  <!-- tremor panel -->
  <g class="panel panel-tremor">
    <text class="panel-heading" x="396" y="629">Social Health Predicts</text>
    <text class="panel-heading" x="396" y="647">Quality of Life More Than Tremor</text>
    <rect x="248" y="675" width="292" height="260" rx="8" fill="url(#chart-bg)"/>
    <g stroke="#f7f7f7" stroke-width="1">
      <line x1="252" x2="538" y1="690" y2="690"/><line x1="252" x2="538" y1="714" y2="714"/>
      <line x1="252" x2="538" y1="738" y2="738"/><line x1="252" x2="538" y1="761" y2="761"/>
      <line x1="252" x2="538" y1="785" y2="785"/><line x1="252" x2="538" y1="809" y2="809"/>
      <line x1="252" x2="538" y1="832" y2="832"/><line x1="252" x2="538" y1="856" y2="856"/>
      <line x1="252" x2="538" y1="880" y2="880"/><line x1="252" x2="538" y1="904" y2="904"/>
    </g>
    <rect x="248" y="920" width="324" height="15" fill="#cfcfcf"/>
    <rect x="540" y="683" width="32" height="14" fill="#cfcfcf"/>
    <text class="tick" x="556" y="694" text-anchor="middle" font-size="9">Severe</text>
    <text class="tick" x="546" y="931" text-anchor="middle" font-size="9">No Tremor</text>
    <g class="tick tick-end" font-size="9.5">
      <text x="537" y="694">100</text><text x="537" y="718">90</text><text x="537" y="742">80</text><text x="537" y="765">70</text>
      <text x="537" y="789">60</text><text x="537" y="813">50</text><text x="537" y="836">40</text><text x="537" y="860">30</text>
      <text x="537" y="884">20</text><text x="537" y="908">10</text>
    </g>
    <g class="tick tick-mid" font-size="9.5">
      <text x="270" y="931">1</text><text x="325" y="931">2</text><text x="381" y="931">3</text><text x="437" y="931">4</text><text x="492" y="931">5</text>
    </g>
    <text class="tick" x="270" y="947" text-anchor="middle">Poor</text>
    <text class="tick" x="495" y="947" text-anchor="middle">Excellent</text>
    <text class="axis-title" x="376" y="969">Quality Of Life</text>
    <text class="axis-title" transform="translate(241 810) rotate(-90)">Percent Responding "True"</text>
    <text class="axis-title" transform="translate(557 808) rotate(-90)">Average Tremor Score</text>

    <g class="series series-tremor">
      <polyline points="268,840 325,845 381,851 437,868 492,880" fill="none" stroke="var(--orange)" stroke-width="1.5"/>
      <g fill="var(--orange)"><circle cx="268" cy="840" r="2.8"/><circle cx="325" cy="845" r="2.8"/><circle cx="381" cy="851" r="2.8"/><circle cx="437" cy="868" r="2.8"/><circle cx="492" cy="880" r="2.8"/></g>
      <g class="point-label" fill="var(--orange)"><text x="268" y="833">37.7</text><text x="325" y="859">36.1</text><text x="381" y="864">31.2</text><text x="439" y="861">25.1</text><text x="493" y="873">20</text></g>
    </g>
    <g class="series series-friends">
      <polyline points="268,848 325,812 381,775 437,752 492,730" fill="none" stroke="#6fae3a" stroke-width="1.5"/>
      <g fill="#6fae3a"><circle cx="268" cy="848" r="2.8"/><circle cx="325" cy="812" r="2.8"/><circle cx="381" cy="775" r="2.8"/><circle cx="437" cy="752" r="2.8"/><circle cx="492" cy="730" r="2.8"/></g>
      <g class="point-label" fill="#6fae3a"><text x="267" y="863">23%</text><text x="325" y="826">38%</text><text x="382" y="769">55%</text><text x="437" y="746">72%</text><text x="491" y="724">84%</text></g>
    </g>
    <g class="series series-lonely">
      <polyline points="268,755 325,797 381,840 437,883 492,896" fill="none" stroke="var(--red)" stroke-width="1.5"/>
      <g fill="var(--red)"><circle cx="268" cy="755" r="2.8"/><circle cx="325" cy="797" r="2.8"/><circle cx="381" cy="840" r="2.8"/><circle cx="437" cy="883" r="2.8"/><circle cx="492" cy="896" r="2.8"/></g>
      <g class="point-label" fill="var(--red)"><text x="284" y="755">73%</text><text x="328" y="790">46%</text><text x="382" y="831">26%</text><text x="437" y="896">8%</text><text x="492" y="909">4%</text></g>
    </g>
    <rect x="267" y="733" width="64" height="12" rx="6" fill="var(--red)"/>
    <text class="pill-text pill-text-sm" x="299" y="742">I am Lonely</text>
    <rect x="374" y="709" width="106" height="12" rx="6" fill="#6fae3a"/>
    <text class="pill-text pill-text-sm" x="427" y="718">I have a lot of Friends</text>
    <rect x="333" y="874" width="82" height="12" rx="6" fill="var(--orange)"/>
    <text class="pill-text pill-text-sm" x="374" y="883">Tremor Severity</text>

    <g class="caption">
      <text x="394" y="996">Overall, individuals identifying as being lonely reported consistently</text>
      <text x="394" y="1009">greater PD symptom severity. Although tremor is a cardinal</text>
      <text x="394" y="1022">symptom of PD and highly visible, feeling socially withdrawn is more</text>
      <text x="394" y="1035">closely correlated to overall quality of life than tremor.</text>
    </g>
  </g>

  <!-- social health bars panel -->
  <g class="panel panel-social">
    <rect x="579" y="596" width="344" height="441" fill="var(--blue-panel)"/>
    <text class="panel-heading" x="749" y="629">Poor Social Health</text>
    <text class="panel-heading" x="749" y="647">Correlates with PD Severity</text>

    <text class="section-label" x="597" y="682" fill="#6a3a94">Social Satisfaction</text>
    <g stroke="#e9f0f7" stroke-width="1">
      <line x1="630" x2="910" y1="698" y2="698"/><line x1="630" x2="910" y1="725" y2="725"/>
      <line x1="630" x2="910" y1="752" y2="752"/><line x1="630" x2="910" y1="779" y2="779"/><line x1="630" x2="910" y1="806" y2="806"/>
    </g>
    <g class="grid-tick"><text x="625" y="701">2000</text><text x="625" y="728">1500</text><text x="625" y="755">1000</text><text x="625" y="782">500</text><text x="625" y="809">0</text></g>
    <g class="question"><text x="633" y="714">In general, please rate how well</text><text x="633" y="725">you rate your satisfaction with your</text><text x="633" y="737">social activites and relationships?</text></g>
    <rect x="665" y="779" width="23" height="27" fill="var(--green)"/>
    <rect x="712" y="770" width="23" height="36" fill="var(--green-mid)"/>
    <rect x="759" y="758" width="23" height="48" fill="var(--green-soft)"/>
    <rect x="806" y="742" width="23" height="64" fill="var(--red-soft)"/>
    <rect x="853" y="735" width="23" height="71" fill="var(--red-deep)"/>
    <g class="bar-value"><text x="676" y="775">494</text><text x="723" y="766">667</text><text x="770" y="754">889</text><text x="817" y="738">1178</text><text x="864" y="731">1317</text></g>
    <g class="bar-name"><text x="676" y="816">Excellent</text><text x="723" y="816">Very Good</text><text x="770" y="816">Good</text><text x="817" y="816">Fair</text><text x="864" y="816">Poor</text>
      <text x="676" y="828">n = 343</text><text x="723" y="828">n = 607</text><text x="770" y="828">n = 468</text><text x="817" y="828">n = 269</text><text x="864" y="828">n = 61</text></g>

    <text class="section-label" x="597" y="864" fill="#2a78c2">Social Performance</text>
    <g stroke="#e9f0f7" stroke-width="1">
      <line x1="630" x2="910" y1="882" y2="882"/><line x1="630" x2="910" y1="909" y2="909"/>
      <line x1="630" x2="910" y1="936" y2="936"/><line x1="630" x2="910" y1="963" y2="963"/><line x1="630" x2="910" y1="990" y2="990"/>
    </g>
    <g class="grid-tick"><text x="625" y="885">2000</text><text x="625" y="912">1500</text><text x="625" y="939">1000</text><text x="625" y="966">500</text><text x="625" y="993">0</text></g>
    <g class="question"><text x="636" y="898">In general, please rate how well</text><text x="636" y="910">you rate your satisfaction with</text><text x="636" y="922">your social activites and roles?</text></g>
    <rect x="665" y="966" width="23" height="24" fill="var(--green)"/>
    <rect x="712" y="955" width="23" height="35" fill="var(--green-mid)"/>
    <rect x="759" y="940" width="23" height="50" fill="var(--green-soft)"/>
    <rect x="806" y="923" width="23" height="67" fill="var(--red-soft)"/>
    <rect x="853" y="911" width="23" height="79" fill="var(--red-deep)"/>
    <g class="bar-value"><text x="676" y="962">446</text><text x="723" y="951">653</text><text x="770" y="936">922</text><text x="817" y="919">1233</text><text x="864" y="907">1464</text></g>
    <g class="bar-name"><text x="676" y="1000">Excellent</text><text x="723" y="1000">Very Good</text><text x="770" y="1000">Good</text><text x="817" y="1000">Fair</text><text x="864" y="1000">Poor</text>
      <text x="676" y="1012">n = 322</text><text x="723" y="1012">n = 647</text><text x="770" y="1012">n = 491</text><text x="817" y="1012">n = 247</text><text x="864" y="1012">n = 44</text></g>
  </g>

  <!-- modifiable variables panel -->
  <g class="panel panel-variables">
    <text class="panel-heading" x="1112" y="629">Modifiable Variables Associated with</text>
    <text class="panel-heading" x="1112" y="647">Rate of PD Progression</text>

    <g class="variable-name" text-anchor="end">
      <text x="1104" y="680">Exercise 30+ min/day, 7 days/wk</text>
      <text x="1104" y="709">Exercise 30+ min/day, 6 days/wk</text>
      <text x="1104" y="736">Exercise 30+ min/day, 5 days/wk</text>
      <text x="1104" y="762">Exercise 30+ min/day, 4 days/wk</text>
      <text x="1104" y="790">Exercise 30+ min/day, 3 days/wk</text>
      <text x="1104" y="817">I have a lot of friends</text>
      <text x="1104" y="845">I cook most of my meals</text>
      <text x="1104" y="871">I practice stress management</text>
    </g>
    <rect x="1002" y="685" width="102" height="10" fill="url(#green-bar)"/>
    <rect x="1005" y="713" width="99" height="10" fill="url(#green-bar)"/>
    <rect x="1023" y="740" width="81" height="10" fill="url(#green-bar)"/>
    <rect x="1026" y="766" width="78" height="10" fill="url(#green-bar)"/>
    <rect x="1039" y="794" width="65" height="10" fill="url(#green-bar)"/>
    <rect x="1047" y="821" width="57" height="10" fill="url(#green-bar)"/>
    <rect x="1054" y="848" width="50" height="10" fill="url(#green-bar)"/>
    <rect x="1088" y="875" width="16" height="10" fill="url(#green-bar)"/>
    <g class="impact-neg" text-anchor="middle">
      <text x="985" y="694">-301</text><text x="988" y="722">-292</text><text x="1007" y="749">-237</text><text x="1010" y="775">-229</text>
      <text x="1022" y="803">-192</text><text x="1032" y="830">-168</text><text x="1036" y="857">-148</text><text x="1076" y="884">-48</text>
    </g>

    <g class="variable-name">
      <text x="1104" y="898">I have a lot of stress</text>
      <text x="1104" y="925">I smoke tobacco</text>
      <text x="1104" y="952">I am overweight</text>
      <text x="1104" y="980">I am lonely</text>
    </g>
    <rect x="1104" y="902" width="47" height="10" fill="url(#red-bar)"/>
    <rect x="1104" y="929" width="59" height="10" fill="url(#red-bar)"/>
    <rect x="1104" y="956" width="61" height="10" fill="url(#red-bar)"/>
    <rect x="1104" y="983" width="112" height="10" fill="url(#red-bar)"/>
    <g class="impact-pos" text-anchor="middle">
      <text x="1163" y="911">139</text><text x="1170" y="938">173</text><text x="1178" y="965">180</text><text x="1228" y="992">328</text>
    </g>

    <rect x="940" y="1003" width="316" height="12" fill="#d6d6d6"/>
    <g class="scale-tick">
      <text x="957" y="1013">-400</text><text x="995" y="1013">-300</text><text x="1033" y="1013">-200</text><text x="1071" y="1013">-100</text>
      <text x="1104" y="1013">0</text><text x="1133" y="1013">100</text><text x="1168" y="1013">200</text><text x="1204" y="1013">300</text><text x="1240" y="1013">400</text>
    </g>
    <g class="scale-end"><text x="958" y="1028">Better than</text><text x="958" y="1038">Average</text><text x="1241" y="1028">Worse than</text><text x="1241" y="1038">Average</text></g>
    <text class="axis-title" x="1104" y="1031">PRO-PD Impact</text>

    <g class="findings">
      <text x="1268" y="684">Individuals who reported feeling</text>
      <text x="1268" y="697">lonely reported greater overall</text>
      <text x="1268" y="710">PD symptom severity (+328;</text>
      <text x="1268" y="723">p=0.000), which was even higher</text>
      <text x="1268" y="737">than scores for smoking tobacco</text>
      <text x="1268" y="750">(+173; p=0.005) and having a lot</text>
      <text x="1268" y="763">of stress(+180; p=0.000).</text>
      <text x="1268" y="785">In contrast, individuals that</text>
      <text x="1268" y="798">reported having a lot of friends</text>
      <text x="1268" y="811">had reduced PD severity scores</text>
      <text x="1268" y="824">(-168; p=0.000). Notably,</text>
      <text x="1268" y="837">exercising 7 days per week was</text>
      <text x="1268" y="850">less beneficial (-301; p=0.000)</text>
      <text x="1268" y="863">than feeling lonely was</text>
      <text x="1268" y="876">detrimental (+328; p=0.000).</text>
    </g>
  </g>
</svg>
</body>
</html>
```